Bref créative
Limb Nestler
Naturally made in the US
Professional
Rosalind Featherstone
Owner
437 Tamsin Ave - Ste 220-581
rfeatherstone@limbnestler-example.com
Limbnestler-example.com
I'm not sure what the first two boxes refer to. I want our logo to be on the cards in the same colors.

```html
<!DOCTYPE html>
<html lang="en">
<head>
<meta charset="utf-8">
<title>Limb Nestler – Stationery Set</title>
<link rel="stylesheet" href="https://fonts.googleapis.com/css2?family=Roboto:wght@400;700&display=swap">
<style>
:root{
  --stage:#3b3b3d;
  --paper:#ffffff;
  --ink:#1b1b1b;
  --muted:#6d6d6d;
  --maroon:#7a1f22;
  --blue:#1c9ce2;
  --black:#121212;
  --rule:#cfcfcf;
}
*{box-sizing:border-box;margin:0;padding:0}
html,body{width:1200px;height:765px;overflow:hidden}
body{background:var(--stage);font-family:"Roboto",Arial,sans-serif;color:var(--ink);position:relative}
.item{position:absolute;background:var(--paper);box-shadow:0 3px 10px rgba(0,0,0,.45);overflow:hidden}

/* brand name block */
.brand{display:flex;align-items:center;gap:4px}
.brand-dot{width:9px;height:9px;border-radius:50%;background:var(--blue);flex:none}
.brand-name{font-weight:700;color:var(--maroon);white-space:nowrap}
.brand-tag{font-size:4px;color:var(--muted);margin-top:1px}
.on-dark .brand-name{color:#fff}
.on-dark .brand-tag{color:rgba(255,255,255,.8)}

/* business cards */
.card{width:122px;height:60px;padding:7px 8px}
.card--black{background:var(--black);color:#fff}
.card--maroon{background:var(--maroon);color:#fff}
.card--blue{background:var(--blue);color:#fff}
.card .brand-name{font-size:9px}
.card-front{display:flex;justify-content:space-between;height:100%}
.card-contact{font-size:4px;line-height:1.45}
.card-contact .person{font-size:5.5px;font-weight:700}
.card-back{display:flex;flex-direction:column;align-items:center;justify-content:center;height:100%}
.card-back .brand-name{font-size:12px}

/* letter & fax */
.sheet{width:262px;height:341px;padding:14px 16px}
.sheet .brand-name{font-size:10px}
.sheet-address{font-size:4px;color:var(--muted);line-height:1.5;margin-top:8px}
.sheet-swoosh{position:absolute;left:0;bottom:0;width:100%;height:44px}
.fax-title{position:absolute;right:18px;top:62px;font-size:12px;font-weight:700}
.fax-table{position:absolute;left:16px;top:78px;width:230px;border-collapse:collapse;font-size:4px}
.fax-table td{border:1px solid var(--rule);height:10px;padding:1px 3px;width:25%}
.fax-note{position:absolute;left:16px;top:136px;font-size:4px;font-weight:700}

/* envelopes */
.envelope{width:185px;height:52px}
.envelope-flap{position:absolute;inset:0;width:100%;height:100%}
.envelope .brand{position:absolute;left:50%;top:8px;transform:translateX(-50%)}
.envelope .brand-name{font-size:9px}
.envelope--maroon .brand-name,.envelope--black .brand-name,.envelope--blue .brand-name{color:#fff}
.note-card{width:185px;height:94px}
.note-card .sheet-address{position:absolute;right:10px;bottom:8px;margin:0;font-size:3.5px}
</style>
</head>
<body>

<!-- top row of business cards -->
<div class="item card card--black on-dark" style="left:293px;top:125px">
  <div class="card-front">
    <div class="card-contact">
      <div class="person">Rosalind Featherstone</div>Owner<br>437 Tamsin Ave - Ste 220-581<br>rfeatherstone@limbnestler-example.com<br>Limbnestler-example.com
    </div>
  </div>
</div>
<div class="item card" style="left:413px;top:125px">
  <div class="card-front">
    <div class="card-contact">
      <div class="person">Rosalind Featherstone</div>Owner<br>437 Tamsin Ave - Ste 220-581<br>Limbnestler-example.com
    </div>
    <div><div class="brand"><span class="brand-name">Limb Nestler</span></div><div class="brand-tag">Naturally made in the US</div></div>
  </div>
</div>
<div class="item card card--maroon on-dark" style="left:550px;top:125px">
  <div class="card-front">
    <div><div class="brand"><span class="brand-name">Limb Nestler</span></div><div class="brand-tag">Naturally made in the US</div></div>
    <div class="card-contact" style="text-align:right">
      <div class="person">Rosalind Featherstone</div>Owner<br>437 Tamsin Ave - Ste 220-581<br>Limbnestler-example.com
    </div>
  </div>
</div>
<div class="item card card--blue on-dark" style="left:680px;top:125px">
  <div class="card-front">
    <div class="card-contact">
      <div class="person">Rosalind Featherstone</div>Owner<br>437 Tamsin Ave - Ste 220-581<br>Limbnestler-example.com
    </div>
    <div><div class="brand"><span class="brand-name">Limb Nestler</span></div></div>
  </div>
</div>

<!-- letterhead -->
<div class="item sheet" style="left:276px;top:216px">
  <div class="brand"><span class="brand-dot"></span><span class="brand-name">Limb Nestler</span></div>
  <div class="brand-tag">Naturally made in the US</div>
  <p class="sheet-address">437 Tamsin Ave - Ste 220-581<br>rfeatherstone@limbnestler-example.com · Limbnestler-example.com</p>
  <svg class="sheet-swoosh" viewBox="0 0 262 44" preserveAspectRatio="none" aria-hidden="true">
    <path d="M0 18 Q130 44 262 8 V44 H0Z" fill="var(--maroon)"/>
    <path d="M0 12 Q140 40 262 0 V7 Q140 46 0 18Z" fill="var(--blue)"/>
  </svg>
</div>

<!-- fax sheet -->
<div class="item sheet" style="left:550px;top:216px">
  <div class="brand"><span class="brand-dot"></span><span class="brand-name">Limb Nestler</span></div>
  <div class="brand-tag">Naturally made in the US</div>
  <p class="sheet-address">437 Tamsin Ave - Ste 220-581<br>rfeatherstone@limbnestler-example.com · Limbnestler-example.com</p>
  <div class="fax-title">FAX</div>
  <table class="fax-table">
    <tr><td>To</td><td></td><td>Fax</td><td></td></tr>
    <tr><td>From</td><td></td><td>Date</td><td></td></tr>
    <tr><td>Phone</td><td></td><td>Pages</td><td></td></tr>
    <tr><td>Re</td><td></td><td>CC</td><td></td></tr>
  </table>
  <div class="fax-note">Comments:</div>
  <svg class="sheet-swoosh" viewBox="0 0 262 44" preserveAspectRatio="none" aria-hidden="true">
    <path d="M0 18 Q130 44 262 8 V44 H0Z" fill="var(--maroon)"/>
    <path d="M0 12 Q140 40 262 0 V7 Q140 46 0 18Z" fill="var(--blue)"/>
  </svg>
</div>

<!-- envelopes -->
<div class="item envelope envelope--blue" style="left:823px;top:216px">
  <svg class="envelope-flap" viewBox="0 0 185 52" preserveAspectRatio="none" aria-hidden="true"><path d="M0 0 H185 V22 Q92 58 0 22Z" fill="var(--blue)"/></svg>
  <div class="brand"><span class="brand-name">Limb Nestler</span></div>
</div>
<div class="item envelope envelope--maroon" style="left:823px;top:268px">
  <svg class="envelope-flap" viewBox="0 0 185 52" preserveAspectRatio="none" aria-hidden="true"><path d="M0 0 H185 V22 Q92 58 0 22Z" fill="var(--maroon)"/></svg>
  <div class="brand"><span class="brand-name">Limb Nestler</span></div>
</div>
<div class="item envelope" style="left:823px;top:320px">
  <svg class="envelope-flap" viewBox="0 0 185 52" preserveAspectRatio="none" aria-hidden="true"><path d="M0 22 Q92 58 185 22" fill="none" stroke="var(--rule)" stroke-width="1"/></svg>
  <div class="brand"><span class="brand-name">Limb Nestler</span></div>
</div>
<div class="item envelope envelope--black" style="left:823px;top:372px">
  <svg class="envelope-flap" viewBox="0 0 185 52" preserveAspectRatio="none" aria-hidden="true"><path d="M0 0 H185 V22 Q92 58 0 22Z" fill="var(--black)"/></svg>
  <div class="brand"><span class="brand-name">Limb Nestler</span></div>
</div>

<!-- small envelope -->
<div class="item note-card" style="left:823px;top:456px">
  <svg class="sheet-swoosh" viewBox="0 0 185 30" preserveAspectRatio="none" style="height:30px;bottom:auto;top:0" aria-hidden="true">
    <path d="M0 0 H185 V6 Q92 22 0 4Z" fill="var(--maroon)"/>
    <path d="M0 4 Q92 22 185 6 V10 Q92 28 0 8Z" fill="var(--blue)"/>
  </svg>
  <p class="sheet-address">437 Tamsin Ave - Ste 220-581 · Limbnestler-example.com</p>
</div>

<!-- bottom row: card backs -->
<div class="item card card--black on-dark" style="left:293px;top:562px">
  <div class="card-back"><div class="brand"><span class="brand-name">Limb Nestler</span></div><div class="brand-tag">Naturally made in the US</div></div>
</div>
<div class="item card" style="left:420px;top:562px">
  <div class="card-back"><div class="brand"><span class="brand-name">Limb Nestler</span></div><div class="brand-tag">Naturally made in the US</div></div>
</div>
<div class="item card card--maroon on-dark" style="left:550px;top:562px">
  <div class="card-back"><div class="brand"><span class="brand-name">Limb Nestler</span></div><div class="brand-tag">Naturally made in the US</div></div>
</div>
<div class="item card card--blue on-dark" style="left:680px;top:562px">
  <div class="card-back"><div class="brand"><span class="brand-name">Limb Nestler</span></div><div class="brand-tag">Naturally made in the US</div></div>
</div>

</body>
</html>
```